Health Benefits Association Website Design

The Unified Household Wellspring Alliance (UHWA) is an organization formed for the purpose of providing its members better value for selected health benefits and services. Members can use the association benefits either in conjunction with or independently of other medical insurance they may have. Some of the benefits available include discounted dental and vision care and prescription mail order services. There is no limitation on who can join. This membership will be primarily marketed as a way to enhance the value of a fixed benefit health insurance plan although members do not have to have the insurance plan join the association.

We are seeking a design for a website to be used for consumers to get information about membership and for current members to be able to access their benefits. The website should include:

1) A landing page to provide a description of the UHWA

2) A secondary page that can be duplicated that will:
a. Provide a list of benefits
b. Provide a membership enrollment form
c. Provide a member’s only access page
d. Provide a contact page for more information

We are seeking a modern but conservative design that will reflect value, simplicity and good health. The site design will also need to be compatible for use with mobile phones and tablets.

A copy of the association logo is included with the submission. It will also need to be incorporated into the website design. Layouts of similar association websites have also been included for reference.

Target Market(s)

Ages 25 to 65 unmarried, married with no children, professionals, self-employed, active and healthy

Industry/Entity Type

Health And Wellness

Number of Pages Required

2 page

Font styles to use
Sans Serif

Colors

Designer to choose colors to be used in the design.

Requirements
Must have
• UHWA Logo (attached). Use colors from the logo in the website design.
Nice to have
• Graphics, if used, should convey health and fitness and skew toward a diverse array of adults 25 to 40.

```html
<!DOCTYPE html>
<html lang="en">
<head>
<meta charset="utf-8">
<title>Unified Household Wellspring Alliance</title>
<link href="https://fonts.googleapis.com/css2?family=Cinzel:wght@400;700&family=Open+Sans:ital,wdth,wght@0,75..100,300..800;1,75..100,300..800&display=swap" rel="stylesheet">
<style>
:root{
  --green:#879b33;
  --green-dark:#75882a;
  --yellow:#fdd20a;
  --yellow-soft:#fde78c;
  --ink:#222;
  --grey-text:#555;
  --panel:#f2f2f2;
  --white:#fff;
}
*{margin:0;padding:0;box-sizing:border-box}
html,body{width:1200px;height:2927px;overflow:hidden}
body{position:relative;font-family:"Open Sans",Arial,sans-serif;color:var(--ink);background:var(--white)}
.abs{position:absolute}
.serif{font-family:"Cinzel",Georgia,serif}

/* header */
.topbar{left:0;top:0;width:1200px;height:43px;background:var(--yellow-soft)}
.topbar .mail{left:78px;top:11px;font-size:15px;color:#5d6b1f;display:flex;align-items:center;gap:12px}
.topbar .login{right:78px;top:11px;font-size:15px;color:#5d6b1f;display:flex;align-items:center;gap:8px}
.nav{left:0;top:43px;width:1200px;height:60px;background:var(--green)}
.nav a{position:absolute;top:0;height:60px;line-height:60px;color:var(--white);text-decoration:none;font-size:16px;text-transform:uppercase}
.nav .active{background:var(--yellow);color:var(--ink);padding:0 26px;left:78px}
.nav .join{background:var(--yellow);color:var(--ink);top:6px;height:48px;line-height:48px;padding:0 20px;font-family:"Cinzel",serif;font-size:21px}
.brand{left:523px;top:0;width:212px;height:185px;z-index:5;background:var(--white);clip-path:polygon(0 0,100% 0,86% 100%,14% 100%);display:flex;flex-direction:column;align-items:center;padding-top:24px;gap:10px}
.brand .dot{width:36px;height:36px;border-radius:50%;background:var(--green)}
.brand .name{font-family:"Cinzel",serif;font-weight:700;color:var(--green);text-align:center;font-size:15px;line-height:1.3;width:150px}

/* hero */
.hero{left:0;top:103px;width:1200px;height:574px;background:
  radial-gradient(ellipse 260px 300px at 900px 260px,#e7d6c8 0%,rgba(231,214,200,0) 100%),
  linear-gradient(90deg,#e9ecef 0%,#dfe3e7 40%,#cfc8c1 68%,#b9aca0 100%)}
.hero h1{left:78px;top:160px;font-weight:300;font-stretch:75%;font-size:60px;line-height:1.08;color:#1c1c1c}
.hero p{left:80px;top:306px;width:500px;font-style:italic;font-size:18px;line-height:1.5;color:#333}
.btn{background:var(--yellow);color:var(--ink);font-family:"Cinzel",serif;font-size:21px;display:flex;align-items:center;justify-content:center;white-space:nowrap}
.hero .btn{left:78px;top:408px;width:176px;height:62px}
.dots{left:553px;top:528px;display:flex;gap:8px}
.dots span{width:18px;height:18px;border-radius:50%;border:2px solid var(--white)}
.dots .on{background:var(--green)}

/* welcome */
.welcome{left:0;top:677px;width:1200px;height:468px;background:var(--panel)}
.welcome .photo{left:0;top:0;width:566px;height:468px;background:
  radial-gradient(ellipse 200px 260px at 200px 220px,#c9a88f 0%,rgba(201,168,143,0) 100%),
  linear-gradient(120deg,#b9c4c8,#e7e5e1 55%,#f7f5f0);clip-path:polygon(0 0,478px 0,566px 468px,0 468px)}
.welcome .mark{left:572px;top:25px;width:60px;height:36px;border-radius:50%;background:var(--green)}
.welcome .kicker{left:572px;top:96px;font-size:20px;color:#333;letter-spacing:1px}
.welcome h2{left:572px;top:120px;font-size:42px;font-weight:400;color:var(--green);white-space:nowrap}
.welcome .sub{left:574px;top:176px;font-size:18px;color:#a4b33e;text-transform:uppercase}
.welcome .copy{left:574px;top:210px;width:560px;font-size:13px;line-height:27px;color:var(--grey-text)}
.welcome .copy p+p{margin-top:8px}
.welcome .btn{left:577px;top:361px;width:176px;height:56px}

/* benefits */
.section-head{left:0;width:1200px;text-align:center}
.section-head .small{font-size:17px;color:#333;font-family:"Cinzel",serif;letter-spacing:1px}
.section-head .big{font-size:44px;color:var(--green);font-family:"Cinzel",serif;line-height:1.1}
.card{width:334px;text-align:center}
.card .pic{width:334px;height:217px}
.card h3{font-family:"Cinzel",serif;font-weight:400;font-size:23px;margin-top:20px;color:#222;letter-spacing:.5px}
.card p{font-size:13.5px;line-height:27px;color:var(--grey-text);margin-top:8px;padding:0 4px}
.card .more{display:inline-flex;align-items:center;gap:4px;margin-top:6px;font-family:"Cinzel",serif;font-size:16px;color:var(--green)}

/* enrollment */
.enroll{left:0;top:1781px;width:1200px;height:332px;background:var(--green)}
.enroll .mark{left:570px;top:34px;width:60px;height:60px;border-radius:50%;background:var(--yellow)}
.enroll h2{left:0;top:102px;width:1200px;text-align:center;font-family:"Cinzel",serif;font-weight:400;font-size:41px;color:var(--white)}
.field{height:48px;background:var(--white);width:291px;font-size:13px;color:#777;padding:0 14px;display:flex;align-items:center}
.submit{height:48px;width:291px;background:var(--yellow);font-family:"Cinzel",serif;font-weight:700;font-size:16px;letter-spacing:1px;display:flex;align-items:center;justify-content:center}

/* news */
.news{width:250px;text-align:center}
.news .pic{width:250px;height:187px;position:relative}
.news .date{position:absolute;right:0;top:0;width:62px;height:74px;background:var(--green);color:var(--white);clip-path:polygon(0 0,100% 0,100% 100%,50% 86%,0 100%);display:flex;flex-direction:column;align-items:center;padding-top:4px}
.news .date b{font-size:30px;font-weight:400;line-height:1.1}
.news .date span{font-family:"Cinzel",serif;font-size:14px}
.news h4{font-family:"Cinzel",serif;font-weight:700;font-size:16px;line-height:25px;margin-top:24px;letter-spacing:.5px}

/* footer */
.footer{left:0;top:2577px;width:1200px;height:291px;background:var(--green);color:var(--white)}
.footer h5{font-family:"Cinzel",serif;font-weight:400;font-size:18px;letter-spacing:1px}
.footer ul{list-style:none;margin-top:20px}
.footer li{font-size:14px;line-height:25.5px;display:flex;align-items:center;gap:12px}
.footer li::before{content:"";width:9px;height:9px;border-radius:50%;background:var(--yellow)}
.footer .hl{color:var(--yellow)}
.contact-row{display:flex;gap:18px;font-size:14px;line-height:26px;margin-top:18px}
.newsitem{display:flex;gap:14px;margin-top:18px;font-size:14px;line-height:22px}
.newsitem .thumb{width:52px;height:52px;border-radius:50%;border:2px solid var(--white);background:linear-gradient(135deg,#b8a98c,#6f7a5a);flex:none}
.bottombar{left:0;top:2868px;width:1200px;height:59px;background:var(--yellow)}
.bottombar .copy{left:78px;top:19px;font-size:14px;color:#333}
.bottombar .brand-s{left:552px;top:-49px;width:92px;height:108px;background:var(--white);clip-path:polygon(0 0,100% 0,84% 100%,16% 100%);display:flex;flex-direction:column;align-items:center;padding-top:12px;gap:4px}
.brand-s .dot{width:20px;height:20px;border-radius:50%;background:var(--green)}
.brand-s .name{font-family:"Cinzel",serif;font-weight:700;color:var(--green);font-size:8px;text-align:center;line-height:1.2;width:64px}
.social{top:8px;width:43px;height:43px;border:2px solid var(--green)}
.social.fill{background:var(--green)}
</style>
</head>
<body>

<header>
  <div class="abs topbar">
    <div class="abs mail">
      <svg width="20" height="15" viewBox="0 0 20 15"><rect x="0" y="0" width="20" height="15" fill="var(--green)"/><path d="M0 0 L10 8 L20 0" stroke="var(--yellow-soft)" stroke-width="2" fill="none"/></svg>
      info@wellspringalliance.org
    </div>
    <div class="abs login">
      <svg width="13" height="16" viewBox="0 0 13 16"><path d="M3 7V4a3.5 3.5 0 0 1 7 0v3" stroke="var(--green)" stroke-width="2" fill="none"/><rect x="0" y="7" width="13" height="9" fill="var(--green)"/></svg>
      Login
    </div>
  </div>
  <nav class="abs nav">
    <a class="active" href="#">Home</a>
    <a href="#" style="left:209px">About</a>
    <a href="#" style="left:289px">Benefits</a>
    <a href="#" style="left:395px">News</a>
    <a href="#" style="left:739px">Charities</a>
    <a href="#" style="left:848px">Membership</a>
    <a class="join" href="#" style="left:997px">Join Us</a>
  </nav>
  <div class="abs brand">
    <span class="dot"></span>
    <span class="name">Unified Household Wellspring Alliance</span>
  </div>
</header>

<section class="abs hero" role="img" aria-label="Smiling older couple embracing at home">
  <h1 class="abs">The Unified Household<br>Wellspring Alliance</h1>
  <p class="abs">UHWA was started to be part of a senior-focused charitable organization that is different from other organizations with a similar perspective or mission.</p>
  <div class="abs btn">Contact Us</div>
  <div class="abs dots"><span></span><span></span><span class="on"></span><span></span></div>
</section>

<section class="abs welcome">
  <div class="abs photo" role="img" aria-label="Woman with a tablet looking out of a bright window"></div>
  <svg class="abs" style="left:478px;top:0" width="92" height="468"><line x1="0" y1="0" x2="88" y2="468" stroke="var(--green)" stroke-width="4"/></svg>
  <div class="abs mark"></div>
  <div class="abs kicker serif">Welcome To</div>
  <h2 class="abs serif">The Unified Household</h2>
  <div class="abs sub">Wellspring Alliance</div>
  <div class="abs copy">
    <p>Welcome to the Unified Household Wellspring Alliance (UHWA). UHWA was started to be part of a senior-focused charitable organization that is different from other organizations with a similar perspective or mission.</p>
    <p>UHWA believes a charity should focus on raising money to support its mission, not its leaders. So, none of the UHWA officers or board members receive any</p>
  </div>
  <div class="abs btn">Know More</div>
</section>

<section>
  <div class="abs section-head" style="top:1205px">
    <div class="small">Our</div>
    <div class="big">Benefits</div>
  </div>
  <article class="abs card" style="left:78px;top:1311px">
    <div class="pic" role="img" aria-label="Older couple reading together at home" style="background:radial-gradient(ellipse 140px 110px at 170px 110px,#e6d8c7,rgba(230,216,199,0)),linear-gradient(135deg,#cfc6b8,#a89780)"></div>
    <h3>DENTAL</h3>
    <p>Lorem Ipsum is simply dummy text of the printing and typesetting industry. Lorem Ipsum has been the industry's standard dummy text ever since the 1500s, when an unknown.</p>
    <div class="more">Read More... <svg width="14" height="12" viewBox="0 0 14 12"><path d="M1 1l5 5-5 5M7 1l5 5-5 5" stroke="var(--green)" stroke-width="2" fill="none"/></svg></div>
  </article>
  <article class="abs card" style="left:433px;top:1311px">
    <div class="pic" role="img" aria-label="Woman relaxing on a beach" style="background:radial-gradient(ellipse 70px 80px at 110px 120px,#d89ab0,rgba(216,154,176,0)),linear-gradient(180deg,#aebfcb,#c9cfd1 45%,#d7c7a6 62%,#c2ad85)"></div>
    <h3>VISION CARE</h3>
    <p>Lorem Ipsum is simply dummy text of the printing and typesetting industry. Lorem Ipsum has been the industry's standard dummy text ever since the 1500s, when an unknown.</p>
    <div class="more">Read More... <svg width="14" height="12" viewBox="0 0 14 12"><path d="M1 1l5 5-5 5M7 1l5 5-5 5" stroke="var(--green)" stroke-width="2" fill="none"/></svg></div>
  </article>
  <article class="abs card" style="left:788px;top:1311px">
    <div class="pic" role="img" aria-label="Young couple looking at a map in a city street" style="background:radial-gradient(ellipse 120px 100px at 130px 140px,#9fb3c8,rgba(159,179,200,0)),linear-gradient(135deg,#d3c9b9,#a3a095)"></div>
    <h3>PRESCRIPTION MAIL ORDER</h3>
    <p>Lorem Ipsum is simply dummy text of the printing and typesetting industry. Lorem Ipsum has been the industry's standard dummy text ever since the 1500s, when an unknown.</p>
    <div class="more">Read More... <svg width="14" height="12" viewBox="0 0 14 12"><path d="M1 1l5 5-5 5M7 1l5 5-5 5" stroke="var(--green)" stroke-width="2" fill="none"/></svg></div>
  </article>
</section>

<section class="abs enroll">
  <div class="abs mark"></div>
  <h2 class="abs">UHWA Membership Enrollment Form</h2>
  <div class="abs field" style="left:150px;top:168px">Name*</div>
  <div class="abs field" style="left:455px;top:168px">Email*</div>
  <div class="abs field" style="left:759px;top:168px">Phone*</div>
  <div class="abs field" style="left:150px;top:230px">Address*</div>
  <div class="abs field" style="left:455px;top:230px">Messsage*</div>
  <div class="abs submit" style="left:759px;top:230px">SUBMIT</div>
</section>

<section>
  <div class="abs section-head" style="top:2173px">
    <div class="small">Latest</div>
    <div class="big">News</div>
  </div>
  <article class="abs news" style="left:78px;top:2271px">
    <div class="pic" role="img" aria-label="Older couple reading on a sofa" style="background:linear-gradient(135deg,#b9ada0,#e0dbd3)"><div class="date"><b>28</b><span>May</span></div></div>
    <h4>LOREM IPSUM IS SIMPLY<br>DUMMY PRINT TEXT</h4>
  </article>
  <article class="abs news" style="left:343px;top:2271px">
    <div class="pic" role="img" aria-label="Woman working on a laptop" style="background:linear-gradient(135deg,#e2e2de,#9b9a96)"><div class="date"><b>29</b><span>May</span></div></div>
    <h4>LOREM IPSUM IS SIMPLY<br>DUMMY PRINT TEXT</h4>
  </article>
  <article class="abs news" style="left:609px;top:2271px">
    <div class="pic" role="img" aria-label="Professional woman on the phone in an office" style="background:linear-gradient(135deg,#f0efec,#b3aea6)"><div class="date"><b>30</b><span>May</span></div></div>
    <h4>LOREM IPSUM IS SIMPLY<br>DUMMY PRINT TEXT</h4>
  </article>
  <article class="abs news" style="left:874px;top:2271px">
    <div class="pic" role="img" aria-label="Two men fishing on a lakeside dock" style="background:linear-gradient(180deg,#c7d3cc,#8f9f86 65%,#a87a6a)"><div class="date"><b>31</b><span>May</span></div></div>
    <h4>LOREM IPSUM IS SIMPLY<br>DUMMY PRINT TEXT</h4>
  </article>
</section>

<footer>
  <div class="abs footer">
    <div class="abs" style="left:78px;top:40px">
      <h5>Usefull Links</h5>
      <ul><li>Home</li><li>About</li><li>Benefits</li><li>News</li><li>Charities</li><li>Membership</li><li>Contact</li></ul>
    </div>
    <div class="abs" style="left:343px;top:40px">
      <h5>Benefits</h5>
      <ul><li>Dental</li><li>Vision Care</li><li>Prescription</li><li>Mail Order</li></ul>
    </div>
    <div class="abs" style="left:609px;top:40px;width:240px">
      <h5>Contact Us</h5>
      <div class="contact-row">
        <svg width="22" height="28" viewBox="0 0 22 28" style="flex:none"><path d="M11 27C11 27 2 16 2 10a9 9 0 0 1 18 0c0 6-9 17-9 17z" stroke="var(--yellow)" stroke-width="2" fill="none"/><circle cx="11" cy="10" r="3" stroke="var(--yellow)" stroke-width="2" fill="none"/></svg>
        <div><span class="hl">The Unified Household</span><br>Lorem Ipsum is simply dummy print text of industry.</div>
      </div>
      <div class="contact-row">
        <svg width="22" height="22" viewBox="0 0 22 22" style="flex:none"><path d="M4 2l4 1 1 5-3 2a12 12 0 0 0 6 6l2-3 5 1 1 4-3 2C10 20 2 12 2 5z" stroke="var(--yellow)" stroke-width="1.8" fill="none"/></svg>
        <div>+100 555 0147</div>
      </div>
      <div class="contact-row">
        <svg width="22" height="17" viewBox="0 0 22 17" style="flex:none"><rect x="1" y="1" width="20" height="15" stroke="var(--yellow)" stroke-width="1.8" fill="none"/><path d="M1 1l10 8 10-8" stroke="var(--yellow)" stroke-width="1.8" fill="none"/></svg>
        <div>info@wellspringalliance.org</div>
      </div>
    </div>
    <div class="abs" style="left:870px;top:40px;width:260px">
      <h5>Latest News</h5>
      <div class="newsitem"><div class="thumb" role="img" aria-label="News thumbnail, person outdoors"></div><div>Lorem Ipsum is simply dummy text of<br><span class="hl">Today 5:60 pm - 30.05.2017</span></div></div>
      <div class="newsitem"><div class="thumb" role="img" aria-label="News thumbnail, portrait"></div><div>Lorem Ipsum is simply dummy text of<br><span class="hl">Today 2:10 pm - 30.05.2017</span></div></div>
    </div>
  </div>
  <div class="abs bottombar">
    <div class="abs copy">©The Unified Household Wellspring - 2017, All rights resreved.</div>
    <div class="abs brand-s"><span class="dot"></span><span class="name">Unified Household Wellspring Alliance</span></div>
    <div class="abs social fill" style="left:976px"></div>
    <div class="abs social" style="left:1028px"></div>
    <div class="abs social" style="left:1081px"></div>
  </div>
</footer>

</body>
</html>
```